Lawn Sign For Construction Projects - Brisk Current

This contest is for a lawn sign that will be placed in the front yard of recently completed construction projects. The goal here is to have a bold advertising sign that is visible from a vehicle driving past.

We are still deciding on the default size for our sign, we also may use multiple sizes. The two sizes we will more than likely be using are: 18"h x 24"w and 24"h x 36"w.

Preference will be given to designers that submit original designs that tie into our current brand and are either in both the size formats listed above or are easy to scale in photoshop or illustrator.

In the files, you will see our logo and an example of a lawn sign.

Please contact us with any questions or comments you may have!

Thank You,
- The Brisk Current Team

Industry/Entity Type

Residential Construction

Colors
34a7d8
ffffff
faa54b

Requirements
Nice to have
• 1. The sign must tie into our current branding and color scheme.
• 2. The sign must be clearly visible and readable.
• 3. The sign must include our phone number in readable print.
• 4. Our website written in small print along the bottom of the sign.
• 5. Must mention we install the following products:
• a.) Solar
• b.) Roofing
• c.) Windows
• d.) Artificial Lawn
• e.) Whole House Fans
• f.) Patio Covers

```html
<!DOCTYPE html>
<html lang="en">
<head>
<meta charset="utf-8">
<title>Brisk Current – Lawn Sign</title>
<link href="https://fonts.googleapis.com/css2?family=Source+Sans+3:wght@400;600;700&display=swap" rel="stylesheet">
<style>
  :root {
    --orange-deep: #f4861f;
    --orange-mid: #f89c1c;
    --orange-warm: #fbb21a;
    --glow: #fffbe8;
    --ink: #000000;
    --brand-blue: #34a7d8;
    --brand-orange: #faa54b;
  }
  html, body {
    margin: 0;
    padding: 0;
    width: 1200px;
    height: 900px;
    overflow: hidden;
    background: #ffffff;
  }
  .lawn-sign {
    display: block;
    width: 1200px;
    height: 900px;
    font-family: "Source Sans 3", "Myriad Pro", Arial, sans-serif;
  }
  .headline-small { font-size: 142px; font-weight: 400; fill: var(--ink); }
  .headline-large { font-size: 292px; font-weight: 700; fill: var(--ink); }
  .phone { font-size: 131px; font-weight: 400; fill: var(--ink); }
  .offer { font-size: 143px; font-weight: 400; fill: var(--ink); }
  .website { font-size: 44px; font-weight: 400; fill: var(--ink); }
  .brand-name { font-size: 56px; font-weight: 600; fill: var(--brand-blue); letter-spacing: -1px; }
  .brand-dot { fill: none; stroke: var(--brand-orange); stroke-width: 7; }
  .corner-band { fill: var(--ink); }
</style>
</head>
<body>
<svg class="lawn-sign" viewBox="0 0 1200 900" xmlns="http://www.w3.org/2000/svg">
  <defs>
    <linearGradient id="sky" x1="0" y1="0" x2="0" y2="1">
      <stop offset="0" stop-color="var(--orange-deep)"/>
      <stop offset="0.55" stop-color="var(--orange-mid)"/>
      <stop offset="1" stop-color="var(--orange-warm)"/>
    </linearGradient>
    <radialGradient id="sun-glow" cx="1130" cy="60" r="520" gradientUnits="userSpaceOnUse">
      <stop offset="0" stop-color="var(--glow)" stop-opacity="1"/>
      <stop offset="0.2" stop-color="var(--glow)" stop-opacity="0.85"/>
      <stop offset="0.55" stop-color="var(--glow)" stop-opacity="0.25"/>
      <stop offset="1" stop-color="var(--glow)" stop-opacity="0"/>
    </radialGradient>
  </defs>

  <g class="backdrop" role="img" aria-label="Warm orange sky with bright sunlight glowing in the top right corner">
    <rect width="1200" height="900" fill="url(#sky)"/>
    <rect width="1200" height="900" fill="url(#sun-glow)"/>
  </g>

  <polygon class="corner-band" points="0,496 840,900 0,900"/>

  <text class="headline-small" x="40" y="178">We’ve Gone</text>
  <text class="headline-large" x="50" y="412">SOLAR</text>
  <text class="phone" x="1156" y="554" text-anchor="end">044-555-0182</text>
  <text class="offer" x="1152" y="774" text-anchor="end">$0 Down</text>
  <text class="website" x="1158" y="858" text-anchor="end">www.brisksite.com</text>

  <g class="brand">
    <circle class="brand-dot" cx="226" cy="724" r="50"/>
    <text class="brand-name" x="226" y="838" text-anchor="middle">Brisk Current</text>
  </g>
</svg>
</body>
</html>
```